Brevanta needs a business Card Design

We are looking for a business card Design for our new Managed Service Provider Company, Brevanta. Brevanta encompasses everything IT for the average medium sized business. Our primary services are help desk support, cyber-security (malware and ransomware protection), and Disaster Recovery systems. We would like the design to have a very clean and professional look, with a very minimalist feel.

Target Market(s)

Medium to large sized businesses

Industry/Entity Type

It Service

Contact Information for Business Card

Name GoesHere
name@brevanta-mail.net
O: 555-382-6047
C: 555-000-0000

Font styles to use
Other font styles liked:
• Poppins Font Only Please

Colors

Designer to choose only greyscale colors for use in the design.

Requirements
Must have
• Logo included
Nice to have
• Cutting Edge, innovative, minimalistic, elegant

```html
<!DOCTYPE html>
<html lang="en">
<head>
<meta charset="UTF-8">
<title>Brevanta Business Card</title>
<link href="https://fonts.googleapis.com/css2?family=Poppins:wght@300;400;500;700&display=swap" rel="stylesheet">
<style>
  :root {
    --navy: #06223a;
    --white: #ffffff;
    --backdrop: #e6e7e9;
    --muted: #1c2f42;
  }
  * { margin: 0; padding: 0; box-sizing: border-box; }
  html, body {
    width: 1200px;
    height: 1000px;
    overflow: hidden;
    background: var(--backdrop);
    font-family: "Poppins", sans-serif;
  }
  .card {
    position: absolute;
    left: 280px;
    width: 640px;
    height: 366px;
    border-radius: 22px;
    box-shadow: 0 6px 18px rgba(0,0,0,0.18);
    overflow: hidden;
  }
  .card--front { top: 90px; background: var(--navy); }
  .card--back { top: 540px; background: var(--white); }

  .wordmark {
    font-weight: 400;
    letter-spacing: 0.55em;
    text-transform: uppercase;
    white-space: nowrap;
  }
  .card--front .wordmark {
    position: absolute;
    top: 50%;
    left: 50%;
    transform: translate(-50%, -50%);
    padding-left: 0.55em;
    color: var(--white);
    font-size: 40px;
  }

  .identity {
    position: absolute;
    left: 48px;
    top: 46px;
    color: var(--navy);
  }
  .identity__name {
    font-weight: 700;
    font-size: 28px;
    line-height: 1.1;
  }
  .identity__title {
    font-weight: 400;
    font-size: 15px;
    margin-top: 4px;
  }
  .card--back .wordmark {
    position: absolute;
    right: 40px;
    top: 92px;
    color: var(--navy);
    font-size: 26px;
  }
  .divider {
    position: absolute;
    left: 48px;
    right: 48px;
    top: 160px;
    height: 2px;
    background: var(--navy);
  }
  .contacts {
    position: absolute;
    left: 48px;
    top: 188px;
    list-style: none;
    color: var(--muted);
    font-weight: 300;
    font-size: 18px;
  }
  .contacts li {
    display: flex;
    align-items: center;
    gap: 12px;
    height: 34px;
  }
  .contacts svg {
    width: 16px;
    height: 16px;
    flex: none;
  }
</style>
</head>
<body>
  <section class="card card--front">
    <div class="wordmark">Brevanta</div>
  </section>

  <section class="card card--back">
    <div class="identity">
      <div class="identity__name">GoesHere</div>
      <div class="identity__title">Managing Director</div>
    </div>
    <div class="wordmark">Brevanta</div>
    <div class="divider"></div>
    <ul class="contacts">
      <li>
        <svg viewBox="0 0 16 16" aria-hidden="true"><path d="M3 1.5 L6 1.5 L7 5 L5.2 6.3 C6 8.2 7.8 10 9.7 10.8 L11 9 L14.5 10 L14.5 13 C14.5 14 13.5 14.8 12.5 14.5 C7 13.5 2.5 9 1.5 3.5 C1.3 2.5 2 1.5 3 1.5 Z" fill="none" stroke="#06223a" stroke-width="1.4" stroke-linejoin="round"/></svg>
        555-382-6047
      </li>
      <li>
        <svg viewBox="0 0 16 16" aria-hidden="true"><rect x="4" y="1" width="8" height="14" rx="1.5" fill="none" stroke="#06223a" stroke-width="1.4"/><line x1="7" y1="12.5" x2="9" y2="12.5" stroke="#06223a" stroke-width="1.4"/></svg>
        555-000-0000
      </li>
      <li>
        <svg viewBox="0 0 16 16" aria-hidden="true"><rect x="1" y="3" width="14" height="10" rx="1" fill="#06223a"/><path d="M2.5 4.5 L8 9 L13.5 4.5" fill="none" stroke="#ffffff" stroke-width="1.3"/></svg>
        name@brevanta-mail.net
      </li>
    </ul>
  </section>
</body>
</html>
```